Business Card design for Founder and CEO of new shoe company

I am looking for a business card design for my new shoe company called Strido.

I am launching the company this April. Strido shoes offers slip-on athletic and casual style shoes for men and women. The unique selling point of the brand is that all of our shoe exist without shoelaces. I have included a link to the website to offer additional information about the company, see product images, and gain inspiration for the design. You can use the store owner password "Strido" to access the website.

www.Strido-shop.example

Thanks,
Dean Porlow

Target Market(s)

Active Men and Women ages 16-45

Industry/Entity Type

Business

Contact Information for Business Card

Dean Porlow
Founder and CEO
www.Strido-shop.example
deanporlow@Strido-shop.example
888-730-1964 / 888-7STRIDO
Strido, LLC
2384 N Tarrow St
Chicago, IL 60614

Requirements
Must have
• Be able to quickly and easily tell that Strido is a shoe company from the business card

```html
<!DOCTYPE html>
<html lang="en">
<head>
<meta charset="utf-8">
<title>Strido Business Card</title>
<link rel="stylesheet" href="https://fonts.googleapis.com/css2?family=Open+Sans:wght@300;400;700&display=swap">
<style>
  :root {
    --backdrop: #e6e3df;
    --card-black: #070707;
    --card-white: #f1f0f0;
    --ink-dark: #1c1c1c;
    --ink-light: #ffffff;
    --ink-muted: #9a9a9a;
    --shadow: rgba(0, 0, 0, 0.18);
  }
  * { box-sizing: border-box; margin: 0; padding: 0; }
  html, body {
    width: 1200px;
    height: 900px;
    overflow: hidden;
    background: var(--backdrop);
    font-family: "Open Sans", Arial, sans-serif;
  }
  .canvas {
    position: relative;
    width: 1200px;
    height: 900px;
  }
  .card {
    position: absolute;
    left: 250px;
    width: 700px;
    height: 400px;
    box-shadow: 0 6px 18px var(--shadow);
  }
  .card--front {
    top: 40px;
    background: var(--card-black);
  }
  .card--back {
    top: 460px;
    background: var(--card-white);
  }
  .wordmark {
    position: absolute;
    font-weight: 300;
    letter-spacing: 1px;
    line-height: 1;
    white-space: nowrap;
  }
  .card--front .wordmark {
    top: 44px;
    right: 56px;
    font-size: 54px;
    color: var(--ink-light);
  }
  .tagline {
    position: absolute;
    top: 112px;
    right: 58px;
    font-size: 13px;
    font-weight: 400;
    letter-spacing: 3px;
    text-transform: uppercase;
    color: var(--ink-muted);
    white-space: nowrap;
  }
  .card--back .wordmark {
    left: 56px;
    bottom: 46px;
    font-size: 58px;
    color: var(--ink-dark);
  }
  .contact {
    position: absolute;
    top: 48px;
    left: 380px;
    color: var(--ink-dark);
    font-size: 13px;
    line-height: 1.4;
    white-space: nowrap;
  }
  .contact__name {
    font-size: 19px;
    font-weight: 700;
    line-height: 1.1;
  }
  .contact__title {
    font-size: 13px;
    margin-bottom: 18px;
  }
  .contact__address {
    margin-bottom: 16px;
  }
  .contact__list {
    list-style: none;
    margin-left: 40px;
  }
  .contact__list li {
    display: flex;
    align-items: center;
    gap: 10px;
    height: 24px;
  }
  .contact__icon {
    width: 12px;
    height: 12px;
    fill: var(--ink-dark);
    flex: none;
  }
</style>
</head>
<body>
<main class="canvas">
  <section class="card card--front" aria-label="Card front">
    <div class="wordmark">Strido</div>
    <p class="tagline">Slip-on shoes</p>
  </section>

  <section class="card card--back" aria-label="Card back">
    <div class="contact">
      <p class="contact__name">Dean Porlow</p>
      <p class="contact__title">Founder and CEO</p>
      <p class="contact__address">Strido, LLC 2384 N Tarrow St<br>Chicago, IL 60614</p>
      <ul class="contact__list">
        <li>
          <svg class="contact__icon" viewBox="0 0 24 24" aria-hidden="true"><path d="M6.6 10.8a15.1 15.1 0 0 0 6.6 6.6l2.2-2.2c.3-.3.7-.4 1-.2 1.1.4 2.3.6 3.6.6.6 0 1 .4 1 1V20c0 .6-.4 1-1 1A17 17 0 0 1 3 4c0-.6.4-1 1-1h3.5c.6 0 1 .4 1 1 0 1.3.2 2.5.6 3.6.1.3 0 .7-.2 1z"/></svg>
          <span>888-730-1964</span>
        </li>
        <li>
          <svg class="contact__icon" viewBox="0 0 24 24" aria-hidden="true"><path d="M6.6 10.8a15.1 15.1 0 0 0 6.6 6.6l2.2-2.2c.3-.3.7-.4 1-.2 1.1.4 2.3.6 3.6.6.6 0 1 .4 1 1V20c0 .6-.4 1-1 1A17 17 0 0 1 3 4c0-.6.4-1 1-1h3.5c.6 0 1 .4 1 1 0 1.3.2 2.5.6 3.6.1.3 0 .7-.2 1z"/></svg>
          <span>888-7STRIDO</span>
        </li>
        <li>
          <svg class="contact__icon" viewBox="0 0 24 24" aria-hidden="true"><path d="M2 6.5V19h20V6.5l-10 7.5z M2.8 5h18.4L12 12z"/></svg>
          <span>deanporlow@Strido-shop.example</span>
        </li>
        <li>
          <svg class="contact__icon" viewBox="0 0 24 24" aria-hidden="true"><circle cx="12" cy="12" r="11"/><path d="M1 12h22M12 1c3 3 4.5 7 4.5 11S15 20 12 23M12 1C9 4 7.5 8 7.5 12S9 20 12 23" fill="none" stroke="#f1f0f0" stroke-width="1.6"/></svg>
          <span>www.Strido-shop.example</span>
        </li>
      </ul>
    </div>
    <div class="wordmark">Strido</div>
  </section>
</main>
</body>
</html>
```